Pharmacy handmade, Personalized Medical Cosmetics Label

Medical Cosmetics label, elegant and professional looking. The creams are Dermatologist formulated and are prepared by local Pharmacy. The label should be versatile and allow space for hand writing to be filled by the pharmacist preparing the product.
The following information will be handwritten:
Upper lid - Lid Balm No.5 ; Marigold, Retinol ; 30
Lower Bottom - Teodora Halvik ; Signature ; 01.01.2017
Upper Lid Label
Velluto Skin (logo)
Doctor Series
(circular pattern - Doctor Formulated, Registered Pharmacy, Handmade, Highest Medical Standards)
(Lid Balm No.5 - in hand writing and different color, maybe red)
Key Ingredients: (Marigold, Retinol - in hand writing, same color as above, maybe red)
(box with hand writing 30) ml
Lower Bottom Label (underneath surface of the container)
Made for Velluto Skin by
Pharmacy Lorant, 7 Pelister blvd., Sofia, ph. 0893517460
Patient: (Teodora Halvik- in hand writing)
Pharmacist: (Signature - in hand writing)
Date: (01.01.2017 - in hand writing)
For External Use
good for 60 days after preparation
Ingredients: Retinol, Marigold Extract, Water, Glycerin, Stearyl Alcohol, Wheat Germ Oil, Polysorbate 60, Sesame Oil, Myristyl Myristate, Cetyl Alcohol, Sorbitan Stearate, Phenoxyethanol, Calendula Extract, Cornflower Extract, Sodium Alginate, Sodium Citrate.
The container lid and bottom are 5 cm = 50 mm in diameter. Made from aluminum and contain 30ml or 50ml.
Please refer to the screen shots from my Web Site to get the feeling for the color pallet and professional look. These creams will be sold on this website. They are custom made by a registered Pharmacy right on the spot after the order has been placed. This is why I need more space for the hand written notes made by the pharmacist who prepared the order.
Please make the design professional, simple and serious colors, like light brown, beige, black or dark brown letters, red hand writing (will be filled by pen or thin marker by the Pharmacist by hand, depending on the order, patient name, etc.)
Thank you.
female 24 - 49 year old
Medical

```html
<!DOCTYPE html>
<html lang="en">
<head>
<meta charset="utf-8">
<title>Velluto Skin – Doctor Series Labels</title>
<link href="https://fonts.googleapis.com/css2?family=Caveat:wght@500&family=Cormorant+SC:wght@500;600&family=Open+Sans:wght@400;600;700&display=swap" rel="stylesheet">
<style>
  :root {
    --paper: #ffffff;
    --ink: #2b2726;
    --ink-soft: #3d3836;
    --pen-red: #c61f2b;
    --rule: #6f6a68;
    --sand-logo: #b39152;
    --stone-logo: #332e2d;
  }
  * { margin: 0; padding: 0; box-sizing: border-box; }
  html, body { width: 818px; height: 1200px; overflow: hidden; background: var(--paper); }
  .sheet { position: relative; width: 818px; height: 1200px; background: var(--paper); }
  .defs { position: absolute; width: 0; height: 0; }

  .label { position: absolute; width: 344px; height: 344px; transform-origin: 50% 50%; }
  .label__ring { position: absolute; inset: 0; }
  .label__ring-text { font-family: "Open Sans", sans-serif; font-size: 15.5px; fill: var(--ink); letter-spacing: 0.4px; }
  .label__content { position: absolute; inset: 0; text-align: center; color: var(--ink); }
  .label__content > * { position: absolute; left: 0; right: 0; }

  .label--sand { --brand: var(--sand-logo); }
  .label--stone { --brand: var(--stone-logo); }

  .brand { display: flex; justify-content: center; align-items: center; gap: 8px;
           font-family: "Open Sans", sans-serif; font-weight: 400; color: var(--brand); }
  .brand__dot { width: 22px; height: 22px; border: 1.5px solid var(--brand); border-radius: 50%; }

  .lid .brand { top: 84px; font-size: 25px; }
  .series { top: 130px; margin: 0 auto; width: 270px; left: 37px; right: auto;
            border-top: 1px solid var(--rule); border-bottom: 1px solid var(--rule);
            font-family: "Cormorant SC", serif; font-weight: 600; font-size: 19px; letter-spacing: 1.5px;
            line-height: 20px; padding-top: 1px; }
  .hand { font-family: "Caveat", cursive; font-weight: 500; color: var(--pen-red); }
  .product { top: 160px; font-size: 29px; }
  .key-label { top: 196px; font-family: "Open Sans", sans-serif; font-size: 13.5px; letter-spacing: 0.5px; }
  .key-items { top: 214px; font-size: 29px; }
  .volume { top: 257px; font-family: "Cormorant SC", serif; font-size: 18px; }
  .volume .hand { font-size: 22px; font-weight: 500; }

  .back .made-for { top: 26px; font-family: "Cormorant SC", serif; font-size: 15px; letter-spacing: 0.5px; }
  .back .brand { top: 50px; font-size: 22px; }
  .pharmacy { top: 86px; font-family: "Open Sans", sans-serif; font-weight: 700; font-size: 10.5px; line-height: 14px; }
  .phone-icon { display: inline-block; width: 8px; height: 9px; vertical-align: -1px; margin-right: 2px; }
  .field { display: flex; justify-content: center; align-items: baseline; gap: 8px; }
  .field__name { font-family: "Open Sans", sans-serif; font-weight: 700; font-size: 10px; }
  .field__value { font-size: 21px; }
  .field--patient { top: 124px; left: -20px; }
  .field--pharmacist { top: 149px; left: -40px; }
  .field--date { top: 173px; left: -30px; }
  .usage { top: 201px; font-family: "Open Sans", sans-serif; font-size: 10.5px; line-height: 14px; }
  .usage--red { color: var(--pen-red); }
  .ingredients-title { top: 229px; font-family: "Open Sans", sans-serif; font-weight: 700; font-size: 12.5px; }
  .ingredients { top: 246px; left: 44px; right: 44px; font-family: "Open Sans", sans-serif; font-size: 9px; line-height: 12.5px; }

  .pos-sand-lid { left: 72px; top: 32px; }
  .pos-sand-back { left: 436px; top: 32px; }
  .pos-stone-lid { left: 60px; top: 448px; }
  .pos-stone-back { left: 444px; top: 448px; }
  .pos-pair-back { left: 440px; top: 800px; transform: scale(0.93); }
  .pos-pair-lid { left: 252px; top: 840px; transform: scale(0.87); }
</style>
</head>
<body>
<main class="sheet">
  <svg class="defs" aria-hidden="true">
    <defs>
      <radialGradient id="petal-sand" cx="50%" cy="50%" r="50%">
        <stop offset="70%" stop-color="#eadcc0"/>
        <stop offset="88%" stop-color="#d9c49c"/>
        <stop offset="100%" stop-color="#efe5d2"/>
      </radialGradient>
      <radialGradient id="petal-stone" cx="50%" cy="50%" r="50%">
        <stop offset="70%" stop-color="#d6d0cd"/>
        <stop offset="88%" stop-color="#b3a9a4"/>
        <stop offset="100%" stop-color="#e0dbd8"/>
      </radialGradient>
      <path id="ring-path" d="M50,172 a122,122 0 1,1 244,0 a122,122 0 1,1 -244,0"/>
    </defs>
  </svg>

  <!-- Sand lid -->
  <section class="label lid label--sand pos-sand-lid">
    <svg class="label__ring" viewBox="0 0 344 344">
      <circle cx="172" cy="172" r="172" fill="url(#petal-sand)" role="img" aria-label="Soft overlapping petal ring in beige"/>
      <circle cx="172" cy="172" r="142" fill="var(--paper)"/>
      <circle cx="172" cy="172" r="117" fill="none" stroke="#8d8785" stroke-width="0.8"/>
      <text class="label__ring-text"><textPath href="#ring-path" startOffset="2%" textLength="740" lengthAdjust="spacing">Doctor Formulated • Registered Pharmacy • Handmade • Highest Medical Standards •</textPath></text>
    </svg>
    <div class="label__content">
      <div class="brand"><span class="brand__dot"></span>Velluto Skin</div>
      <div class="series">Doctor Series</div>
      <div class="product hand">Lid Balm No.5</div>
      <div class="key-label">KEY INGREDIENTS:</div>
      <div class="key-items hand">Marigold, Retinol</div>
      <div class="volume"><span class="hand">30</span> ml</div>
    </div>
  </section>

  <!-- Sand back -->
  <section class="label back label--sand pos-sand-back">
    <svg class="label__ring" viewBox="0 0 344 344">
      <circle cx="172" cy="172" r="172" fill="url(#petal-sand)" role="img" aria-label="Soft overlapping petal ring in beige"/>
      <circle cx="172" cy="172" r="152" fill="var(--paper)"/>
    </svg>
    <div class="label__content">
      <div class="made-for">Made For</div>
      <div class="brand"><span class="brand__dot"></span>Velluto Skin</div>
      <div class="pharmacy">Pharmacy Lorant, 7 Pelister blvd., Sofia,<br><svg class="phone-icon" viewBox="0 0 8 9"><path d="M1.5 0.5 L3 2.5 L2.2 3.4 Q3.2 5.6 4.8 6.4 L5.7 5.6 L7.6 7 L6.6 8.4 Q2.8 8.2 0.6 1.8 Z" fill="currentColor"/></svg>0893517460</div>
      <div class="field field--patient"><span class="field__name">Patient:</span><span class="field__value hand">Teodora Halvik</span></div>
      <div class="field field--pharmacist"><span class="field__name">Pharmacist:</span><span class="field__value hand">Signature</span></div>
      <div class="field field--date"><span class="field__name">Date:</span><span class="field__value hand">01.01.2017</span></div>
      <div class="usage">For External Use<br>Good for 60 days after preparation</div>
      <div class="ingredients-title">Ingredients:</div>
      <div class="ingredients">Retinol, Marigold Extract, Water, Glycerin, Stearyl Alcohol, Wheat Germ Oil, Polysorbate 60, Sesame Oil, Myristyl Myristate, Cetyl Alcohol, Sorbitan Stearate, Phenoxyethanol, Calendula Extract, Cornflower Extract, Sodium Alginate, Sodium Citrate.</div>
    </div>
  </section>

  <!-- Stone lid -->
  <section class="label lid label--stone pos-stone-lid">
    <svg class="label__ring" viewBox="0 0 344 344">
      <circle cx="172" cy="172" r="172" fill="url(#petal-stone)" role="img" aria-label="Soft overlapping petal ring in taupe grey"/>
      <circle cx="172" cy="172" r="142" fill="var(--paper)"/>
      <circle cx="172" cy="172" r="117" fill="none" stroke="#8d8785" stroke-width="0.8"/>
      <text class="label__ring-text"><textPath href="#ring-path" startOffset="2%" textLength="740" lengthAdjust="spacing">Doctor Formulated • Registered Pharmacy • Handmade • Highest Medical Standards •</textPath></text>
    </svg>
    <div class="label__content">
      <div class="brand"><span class="brand__dot"></span>Velluto Skin</div>
      <div class="series">Doctor Series</div>
      <div class="product hand">Lid Balm No.5</div>
      <div class="key-label">KEY INGREDIENTS:</div>
      <div class="key-items hand">Marigold, Retinol</div>
      <div class="volume"><span class="hand">30</span> ml</div>
    </div>
  </section>

  <!-- Stone back -->
  <section class="label back label--stone pos-stone-back">
    <svg class="label__ring" viewBox="0 0 344 344">
      <circle cx="172" cy="172" r="172" fill="url(#petal-stone)" role="img" aria-label="Soft overlapping petal ring in taupe grey"/>
      <circle cx="172" cy="172" r="152" fill="var(--paper)"/>
    </svg>
    <div class="label__content">
      <div class="made-for">Made For</div>
      <div class="brand"><span class="brand__dot"></span>Velluto Skin</div>
      <div class="pharmacy">Pharmacy Lorant, 7 Pelister blvd., Sofia,<br><svg class="phone-icon" viewBox="0 0 8 9"><path d="M1.5 0.5 L3 2.5 L2.2 3.4 Q3.2 5.6 4.8 6.4 L5.7 5.6 L7.6 7 L6.6 8.4 Q2.8 8.2 0.6 1.8 Z" fill="currentColor"/></svg>0893517460</div>
      <div class="field field--patient"><span class="field__name">Patient:</span><span class="field__value hand">Teodora Halvik</span></div>
      <div class="field field--pharmacist"><span class="field__name">Pharmacist:</span><span class="field__value hand">Signature</span></div>
      <div class="field field--date"><span class="field__name">Date:</span><span class="field__value hand">01.01.2017</span></div>
      <div class="usage">For External Use<br><span class="usage--red">Good for 60 days after preparation</span></div>
      <div class="ingredients-title">Ingredients:</div>
      <div class="ingredients">Retinol, Marigold Extract, Water, Glycerin, Stearyl Alcohol, Wheat Germ Oil, Polysorbate 60, Sesame Oil, Myristyl Myristate, Cetyl Alcohol, Sorbitan Stearate, Phenoxyethanol, Calendula Extract, Cornflower Extract, Sodium Alginate, Sodium Citrate.</div>
    </div>
  </section>

  <!-- Pair: back label -->
  <section class="label back label--stone pos-pair-back">
    <svg class="label__ring" viewBox="0 0 344 344">
      <circle cx="172" cy="172" r="172" fill="url(#petal-stone)" role="img" aria-label="Soft overlapping petal ring in taupe grey"/>
      <circle cx="172" cy="172" r="152" fill="var(--paper)"/>
    </svg>
    <div class="label__content">
      <div class="made-for">Made For</div>
      <div class="brand"><span class="brand__dot"></span>Velluto Skin</div>
      <div class="pharmacy">Pharmacy Lorant, 7 Pelister blvd., Sofia,<br><svg class="phone-icon" viewBox="0 0 8 9"><path d="M1.5 0.5 L3 2.5 L2.2 3.4 Q3.2 5.6 4.8 6.4 L5.7 5.6 L7.6 7 L6.6 8.4 Q2.8 8.2 0.6 1.8 Z" fill="currentColor"/></svg>0893517460</div>
      <div class="field field--patient"><span class="field__name">Patient:</span><span class="field__value hand">Teodora Halvik</span></div>
      <div class="field field--pharmacist"><span class="field__name">Pharmacist:</span><span class="field__value hand">Signature</span></div>
      <div class="field field--date"><span class="field__name">Date:</span><span class="field__value hand">01.01.2017</span></div>
      <div class="usage usage--red">For External Use<br>Good for 60 days after preparation</div>
      <div class="ingredients-title">Ingredients:</div>
      <div class="ingredients">Retinol, Marigold Extract, Water, Glycerin, Stearyl Alcohol, Wheat Germ Oil, Polysorbate 60, Sesame Oil, Myristyl Myristate, Cetyl Alcohol, Sorbitan Stearate, Phenoxyethanol, Calendula Extract, Cornflower Extract, Sodium Alginate, Sodium Citrate.</div>
    </div>
  </section>

  <!-- Pair: lid label -->
  <section class="label lid label--stone pos-pair-lid">
    <svg class="label__ring" viewBox="0 0 344 344">
      <circle cx="172" cy="172" r="172" fill="url(#petal-stone)" role="img" aria-label="Soft overlapping petal ring in taupe grey"/>
      <circle cx="172" cy="172" r="142" fill="var(--paper)"/>
      <circle cx="172" cy="172" r="117" fill="none" stroke="#8d8785" stroke-width="0.8"/>
      <text class="label__ring-text"><textPath href="#ring-path" startOffset="2%" textLength="740" lengthAdjust="spacing">Doctor Formulated • Registered Pharmacy • Handmade • Highest Medical Standards •</textPath></text>
    </svg>
    <div class="label__content">
      <div class="brand"><span class="brand__dot"></span>Velluto Skin</div>
      <div class="series">Doctor Series</div>
      <div class="product hand">Lid Balm No.5</div>
      <div class="key-label">KEY INGREDIENTS:</div>
      <div class="key-items hand">Marigold, Retinol</div>
      <div class="volume"><span class="hand">30</span> ml</div>
    </div>
  </section>
</main>
</body>
</html>
```